Vendora Size Charts - 6 Products

Hi Teodor,

I had you in mind for this, but we have a new e-commerce store that requires the attached 6 size charts re-designed. They are terrible charts from drop shippers and we need them re-designed to match the Palvizo brand logo to designed.

Chart needs to be white background and black letter's. You can add some smart gradients or design to it if you want to make it look elegant and confident.

Can you design 1 chart and we can amend it to perfection with feedback?
Once we agree on the style - you can then do the same style and design for the remaining charts.

Let me know if this is ok?

```html
<!DOCTYPE html>
<html lang="en">
<head>
<meta charset="utf-8">
<title>Size Chart</title>
<link rel="stylesheet" href="https://fonts.googleapis.com/css2?family=Roboto:wght@400;700&display=swap">
<style>
  :root {
    --page-bg: #ffffff;
    --panel-bg: #e6e6e6;
    --row-bg: #ffffff;
    --ink: #000000;
    --divider: #c9c9c9;
    --size-s: #fdf07a;
    --size-m: #fecb82;
    --size-l: #fe8866;
    --size-xl: #e57373;
  }
  * { box-sizing: border-box; margin: 0; padding: 0; }
  html, body {
    width: 1200px;
    height: 1000px;
    overflow: hidden;
    background: var(--page-bg);
    font-family: "Roboto", Arial, sans-serif;
    color: var(--ink);
  }
  .canvas { position: relative; width: 1200px; height: 1000px; }

  .chart {
    position: absolute;
    left: 301px; top: 171px;
    width: 598px; height: 510px;
    background: var(--panel-bg);
  }
  .chart-head {
    position: absolute;
    left: 0; top: 21px;
    width: 100%; height: 54px;
  }
  .head-label {
    position: absolute;
    top: 0; height: 54px;
    line-height: 54px;
    font-weight: 700;
    font-size: 20px;
    text-align: center;
  }
  .col-size { left: 32px; width: 161px; }
  .col-bust { left: 195px; width: 190px; }
  .col-length { left: 387px; width: 192px; }

  .divider {
    position: absolute;
    width: 4px;
    border-radius: 2px;
    background: var(--divider);
  }
  .chart-head .divider { top: 0; height: 54px; }
  .divider.first { left: 191px; }
  .divider.second { left: 383px; }

  .size-row {
    position: absolute;
    left: 32px;
    width: 547px; height: 71px;
    background: var(--row-bg);
  }
  .size-row .divider { top: 10px; height: 53px; }
  .size-row .divider.first { left: 159px; }
  .size-row .divider.second { left: 351px; }
  .row-s { top: 98px; }
  .row-m { top: 202px; }
  .row-l { top: 306px; }
  .row-xl { top: 409px; }

  .size-badge {
    position: absolute;
    left: 37px; top: -5px;
    width: 82px; height: 82px;
    border-radius: 50%;
    display: flex; align-items: center; justify-content: center;
    font-size: 42px;
    font-weight: 400;
    letter-spacing: -1px;
  }
  .row-s .size-badge { background: var(--size-s); top: -5px; }
  .row-m .size-badge { background: var(--size-m); top: -5px; }
  .row-l .size-badge { background: var(--size-l); top: -5px; }
  .row-xl .size-badge { background: var(--size-xl); top: -5px; }

  .measure {
    position: absolute;
    top: 0; height: 71px;
    line-height: 71px;
    font-size: 20px;
    text-align: center;
  }
  .measure.bust { left: 163px; width: 188px; }
  .measure.length { left: 355px; width: 192px; }
  .row-l .measure.length { font-size: 22px; }

  .notes {
    position: absolute;
    left: 301px; top: 698px;
    width: 598px; height: 130px;
    background: var(--panel-bg);
    font-size: 14.5px;
    line-height: 20px;
  }
  .note { position: absolute; left: 0; width: 100%; }
  .note-mark {
    position: absolute;
    left: 18px;
    font-size: 18px;
  }
  .note-primary { top: 10px; }
  .note-primary p { margin-left: 46px; width: 545px; }
  .note-secondary { top: 97px; }
  .note-secondary .note-mark { top: -2px; }
  .note-secondary p { margin-left: 44px; }
</style>
</head>
<body>
<div class="canvas">
  <section class="chart" aria-label="Asian size chart">
    <div class="chart-head">
      <div class="head-label col-size">ASIAN SIZE</div>
      <span class="divider first"></span>
      <div class="head-label col-bust">BUST</div>
      <span class="divider second"></span>
      <div class="head-label col-length">LENGTH</div>
    </div>

    <div class="size-row row-s">
      <div class="size-badge">S</div>
      <span class="divider first"></span>
      <div class="measure bust">80cm/31.5"</div>
      <span class="divider second"></span>
      <div class="measure length">80cm/31.5"</div>
    </div>

    <div class="size-row row-m">
      <div class="size-badge">M</div>
      <span class="divider first"></span>
      <div class="measure bust">84cm/33.1"</div>
      <span class="divider second"></span>
      <div class="measure length">82cm/32.2"</div>
    </div>

    <div class="size-row row-l">
      <div class="size-badge">L</div>
      <span class="divider first"></span>
      <div class="measure bust">88cm/34.6"</div>
      <span class="divider second"></span>
      <div class="measure length">84cm/33.1"</div>
    </div>

    <div class="size-row row-xl">
      <div class="size-badge">XL</div>
      <span class="divider first"></span>
      <div class="measure bust">92cm/36.2"</div>
      <span class="divider second"></span>
      <div class="measure length">86cm/33.8"</div>
    </div>
  </section>

  <aside class="notes">
    <div class="note note-primary">
      <span class="note-mark">*</span>
      <p>To make sure you get the right size, please refer to our size chart before bying, if you are not sure about size, please email us your body measurement, so we can give you some suggestions on how to choose the righ size, thanks for understanding</p>
    </div>
    <div class="note note-secondary">
      <span class="note-mark">**</span>
      <p>Mansual measurement may exsit 1-3cm difference.</p>
    </div>
  </aside>
</div>
</body>
</html>
```